IT Consulting Business needs a web design

We need a web design for an IT Consulting company called "Vorenix". We want to replace the existing web site (www.vorenix-example.com) with a new design. Our services are IT Consulting, IT Training, IT Outsourcing.
We would like to see designs that communicate "Trusted IT Advisor" with modern & bold design.

We would like to see the design of 2 pages:
1. Home page (www.vorenix-example.com)
2. The detail page (http://www.vorenix-example.com/index_files/consulting.htm)

Industry/Entity Type

Business

```html
<!DOCTYPE html>
<html lang="en">
<head>
<meta charset="utf-8">
<title>Vorenix – IT Consulting</title>
<link href="https://fonts.googleapis.com/css2?family=Roboto:wght@400;500;700&family=Noto+Sans:wght@300;400&family=Roboto+Condensed:wght@700&display=swap" rel="stylesheet">
<style>
:root{
  --blue:#1f5fb8;
  --blue-bright:#2f86e6;
  --blue-deep:#1863c8;
  --red:#d3282b;
  --text:#333333;
  --page:#f4f4f4;
  --panel:#e4e4e4;
  --footer:#292929;
  --rule:#d6d6d6;
}
*{margin:0;padding:0;box-sizing:border-box}
html,body{width:1200px;height:1051px;overflow:hidden;background:var(--page)}
body{font-family:"Noto Sans",Tahoma,sans-serif;color:var(--text);position:relative}
.site-header{position:absolute;left:0;top:0;width:1200px;height:70px;background:var(--page);border-bottom:3px solid var(--rule)}
.brand{position:absolute;left:188px;top:12px;font-family:"Roboto",sans-serif;font-weight:700;font-size:33px;color:var(--blue);letter-spacing:-0.5px}
.main-nav{position:absolute;left:550px;top:0;display:flex;height:66px}
.main-nav a{display:flex;align-items:center;padding:0 13px;font-family:"Roboto",sans-serif;font-size:12px;color:#555;text-decoration:none;border-left:1px solid #e4e4e4}
.main-nav a:nth-child(2){border-left:none}
.main-nav a.active{background:var(--blue-deep);color:#fff;border-top:5px solid var(--red);padding:0 14px}
.hero{position:absolute;left:0;top:70px;width:1200px;height:383px;background:radial-gradient(ellipse 520px 300px at 800px 190px,#3d93f0 0%,var(--blue-bright) 35%,#1d68cc 100%)}
.hero-visual{position:absolute;left:188px;top:57px;width:481px;height:260px;border-radius:10px 10px 4px 4px;background:linear-gradient(180deg,#3a3a3a 0%,#8a8a8a 55%,#cfcfcf 100%)}
.hero-dots{position:absolute;left:399px;top:333px;display:flex;gap:10px}
.hero-dots span{width:13px;height:13px;border-radius:50%;background:#fff;box-shadow:inset 2px 2px 0 #1a3f7a}
.hero-copy{position:absolute;right:189px;top:143px;width:360px;text-align:right;color:#fff}
.hero-copy h1{font-family:"Roboto Condensed",sans-serif;font-size:19.5px;font-weight:700;letter-spacing:-0.2px}
.hero-copy p{margin-top:10px;font-family:"Noto Sans",sans-serif;font-size:11px;line-height:15.5px}
.content{position:absolute;left:188px;top:474px;width:545px}
.section-title{font-family:"Roboto",sans-serif;font-weight:700;font-size:17px}
.section-title .hl{color:var(--red)}
.section-title .tone{color:var(--blue)}
.intro{margin-top:8px;font-size:10.8px;font-weight:300;line-height:15.4px}
.sub-head{color:var(--red);font-size:10.8px;font-weight:300;margin-top:5px}
.check-list{list-style:none;margin:3px 0 2px 19px}
.check-list li{position:relative;padding-left:12px;font-size:10.8px;font-weight:300;line-height:23.6px}
.check-list li::before{content:"";position:absolute;left:0;top:9px;width:4px;height:4px;border-right:2px solid var(--red);border-top:2px solid var(--red);transform:rotate(45deg)}
.sidebar-box{position:absolute;left:766px;width:245px;background:var(--panel);border-radius:3px;padding:8px 0 0 19px;box-shadow:-4px 0 6px rgba(0,0,0,.08)}
.sidebar-box h2{font-family:"Roboto",sans-serif;font-weight:700;font-size:17px;margin-bottom:7px}
.sidebar-box ul{list-style:none}
.sidebar-box li{position:relative;padding-left:22px;font-size:10.8px;font-weight:300;line-height:18px;margin-bottom:5.5px;padding-right:20px}
.sidebar-box li::before{content:"";position:absolute;left:3px;top:6px;width:7px;height:7px;background:
 radial-gradient(circle,var(--red) 1.2px,transparent 1.5px) 0 0/3.5px 3.5px}
.sidebar-box li.current{color:var(--red);font-weight:400}
.box-services{top:467px;height:122px}
.box-expertise{top:599px;height:211px}
.box-values{top:821px;height:122px}
.site-footer{position:absolute;left:0;top:969px;width:1200px;height:82px;background:var(--footer);font-family:"Roboto",Arial,sans-serif;color:#fff;font-size:11px}
.footer-nav{position:absolute;left:187px;top:18px;display:flex}
.footer-nav a{color:#fff;text-decoration:none}
.footer-nav a.active{color:var(--red)}
.footer-nav .sep{margin:0 10px}
.copyright{position:absolute;left:187px;top:36px}
.social{position:absolute;left:929px;top:18px;display:flex;gap:3.5px}
.social span{width:25px;height:25px;border-radius:3px;background:var(--red)}
</style>
</head>
<body>
<header class="site-header">
  <div class="brand">Vorenix</div>
  <nav class="main-nav">
    <a class="active" href="#">HOME</a>
    <a href="#">ABOUT US</a>
    <a href="#">SERVICES</a>
    <a href="#">EXPERTISES</a>
    <a href="#">CAREERS</a>
    <a href="#">CONTACT US</a>
  </nav>
</header>

<section class="hero">
  <div class="hero-visual" role="img" aria-label="Laptop showing a consultant touching a digital interface"></div>
  <div class="hero-dots"><span></span><span></span><span></span></div>
  <div class="hero-copy">
    <h1>YOUR MOST TRUSTED IT CONSULTANT</h1>
    <p>We are experienced, certified professionals who are experts at Information Technology (IT) consulting, solution design &amp; development, and training for medium-size businesses and large enterprises.</p>
  </div>
</section>

<main class="content">
  <h2 class="section-title"><span class="hl">Consulting</span> <span class="tone">Services</span></h2>
  <p class="intro">Our experienced, certified professionals provides IT consulting using industry recommended practices. We are specialized in Corvane Business Productivity Platform using Corvane ShareDock Technologies and Business Intelligence Platform.</p>
  <p class="sub-head">Some of our services are</p>
  <ul class="check-list">
    <li>Strategic technology consulting and advice</li>
    <li>Business technology reviews, audits, and studies</li>
    <li>Business technology improvements</li>
    <li>Solution architecture design and implementation for applications of all sizes</li>
  </ul>
  <p class="sub-head">Some of our solutions are</p>
  <ul class="check-list">
    <li>Corporate intranet portal and public web site</li>
    <li>Business intelligence solution</li>
    <li>Enterprise search solution</li>
    <li>Document and record management solution</li>
    <li>Business form and enterprise collaboration solution</li>
    <li>Knowledge management solution</li>
  </ul>
</main>

<aside class="sidebar-box box-services">
  <h2 class="section-title"><span class="hl">Our</span> <span class="tone">Services</span></h2>
  <ul>
    <li class="current">Consulting Service</li>
    <li>Training Service</li>
    <li>Solution Service</li>
  </ul>
</aside>
<aside class="sidebar-box box-expertise">
  <h2 class="section-title"><span class="hl">Our</span> <span class="tone">Expertises</span></h2>
  <ul>
    <li>Corvane ShareDock Technologies</li>
    <li>Business Intelligence with Corvane QueryBase Server</li>
    <li>Enterprise Integration with LinkFlow Server</li>
    <li>CoreStack Development</li>
    <li>Q7 DarkOpal</li>
  </ul>
</aside>
<aside class="sidebar-box box-values">
  <h2 class="section-title"><span class="hl">Core</span> <span class="tone">Value</span></h2>
  <ul>
    <li>Quality Conscious</li>
    <li>Customer Fouce</li>
    <li>Committed</li>
  </ul>
</aside>

<footer class="site-footer">
  <nav class="footer-nav">
    <a class="active" href="#">Home</a><span class="sep">|</span>
    <a href="#">About Us</a><span class="sep">|</span>
    <a href="#">Services</a><span class="sep">|</span>
    <a href="#">Careers</a><span class="sep">|</span>
    <a href="#">Expertises</a><span class="sep">|</span>
    <a href="#">Contact Us</a>
  </nav>
  <p class="copyright">Vorenix © 2013. All Rights Reserved.</p>
  <div class="social" aria-label="Social links"><span></span><span></span><span></span></div>
</footer>
</body>
</html>
```